Label Design for Climbing Chalk (fitness category)

I am looking for someone to design a front and back label for a bottle of liquid chalk. Liquid chalk is used in gyms, gymnastics, climbing to prevent your hands from getting moist and increase friction. I'm uploading some design motivations that I like.

The bottle is going to be black and I want the label to be clear. You have free reign of how you want to approach this design. Below are more specifics for the sizing:

*Attached is a picture of a competitor product (Tor Hold Liquid Chalk). Please don't use this for motivation, their label is very bad. I'm attaching a picture so that you can see what the bottle looks like.
*Attached are design motivations that I like
*The bottle is 50 ml, it's 3.75 inches tall, 2 inches wide and 1.25 inches in depth.
*The label can be square or oval (it's up to you). The size of the label needs to be 1,25 x 2.25 inches.
*Name of the product: Varnel Liquid Chalk
*Label needs to have the following Required Text. You can arrange it however you like:
- (50 ml)
- Made by USA Competitive Athletes for Athletes. Increases grip and lasts 3-4 times longer than regular chalk.
- Directions: Shake well. Squeeze some Varnel Liquid Chalk into your hand and rub your hands together. Let your hands air dry for about 10 seconds. To remove the chalk wash your hands with light soap.
Warning: Avoid contact with Eyes. Do not use on broken skin. Do not ingest. Keep out of reach of small children.
- Ingredients: Magnesium carbonate, SD Alcohol, hydroxypropylcellulose, colophonium.

Target Market(s)

Fitness, Athletes, Rock Climbers, Weight Lifters, Gymnasts, etc

Industry/Entity Type

Fitness

Font styles to use
Sans Serif

Colors

Designer to choose colors to be used in the design.

Requirements
Must have
• Please see Project Description for required text. The bottle is going to be black and I want the clear label so please be creative with the colors that would look good
Nice to have
• Please see attached branding ideas that I liked for font and colors. You don't have to strictly stick to them, these are just some of the ones I liked. Be creative and put your best foot forward.

```html
<!DOCTYPE html>
<html lang="en">
<head>
<meta charset="utf-8">
<title>Varnel Liquid Chalk – Label Set</title>
<link rel="stylesheet" href="https://fonts.googleapis.com/css2?family=Exo+2:wght@800&family=Open+Sans:ital,wght@0,400;0,600;1,600;1,700&display=swap">
<style>
  :root {
    --label-red: #931b20;
    --label-red-dark: #7e151a;
    --stone-light: #ececec;
    --stone-mid: #d3d3d3;
    --ink-white: #ffffff;
    --badge-orange: #f2a51c;
    --badge-orange-dark: #c8780c;
    --badge-ink: #5a2a08;
    --page: #ffffff;
  }
  * { box-sizing: border-box; margin: 0; padding: 0; }
  html, body { width: 1200px; height: 750px; overflow: hidden; background: var(--page); }
  .canvas {
    position: relative; width: 1200px; height: 750px;
    display: flex; justify-content: center; align-items: center; gap: 100px;
  }
  .label {
    position: relative; width: 300px; height: 540px;
    border-radius: 18px; overflow: hidden; background: var(--label-red);
  }

  /* Front */
  .front-split { position: absolute; inset: 0; width: 100%; height: 100%; }
  .brand-mark {
    position: absolute; left: 112px; top: 28px; width: 76px; height: 76px;
    border-radius: 50%; background: var(--ink-white);
  }
  .product-name {
    position: absolute; left: 34px; top: 138px; width: 190px;
    font-family: "Exo 2", sans-serif; font-weight: 800; color: var(--ink-white);
    text-align: right; line-height: 1.02; text-transform: uppercase;
  }
  .product-name .brand { display: block; font-size: 32px; }
  .product-name .kind { display: block; font-size: 40px; }
  .climber-art {
    position: absolute; left: 78px; top: 300px; width: 150px; height: 150px;
    border-radius: 10px;
    background: radial-gradient(circle at 50% 45%, rgba(255,255,255,0.85), rgba(255,255,255,0.15) 70%);
  }
  .sport-icons {
    position: absolute; left: 54px; top: 472px; display: flex; gap: 7px;
  }
  .sport-icon {
    width: 31px; height: 31px; border-radius: 5px; background: var(--ink-white);
  }

  /* Back */
  .back-copy {
    position: absolute; left: 30px; top: 34px; width: 240px;
    font-family: "Open Sans", sans-serif; color: var(--ink-white);
    font-size: 11.4px; font-weight: 600; line-height: 1.37; text-align: justify;
  }
  .back-copy p { margin-bottom: 14px; }
  .back-copy .intro { padding-bottom: 8px; border-bottom: 1.5px solid var(--ink-white); margin-bottom: 10px; }
  .back-copy em { font-style: italic; font-weight: 700; }
  .cautions { font-weight: 400; font-size: 10.6px; text-align: left; list-style: none; }
  .cautions-title { font-style: italic; font-weight: 700; font-size: 10.6px; margin-bottom: 2px; }
  .cautions li { position: relative; padding-left: 13px; }
  .cautions li::before {
    content: ""; position: absolute; left: 2px; top: 6px;
    width: 5px; height: 5px; border-radius: 50%; background: var(--ink-white);
  }
  .back-badges {
    position: absolute; left: 30px; right: 22px; bottom: 40px;
    display: flex; align-items: center; gap: 8px;
  }
  .pill {
    font-family: "Open Sans", sans-serif; font-weight: 700; font-style: italic;
    color: var(--badge-ink); background: var(--badge-orange);
    border: 2px solid var(--badge-orange-dark); border-radius: 5px;
    padding: 3px 6px; line-height: 1;
  }
  .pill.no-mess { font-size: 9.5px; padding: 6px 6px; }
  .pill.volume { font-size: 15px; }
  .origin-badge {
    margin-left: auto; width: 70px; height: 70px; border-radius: 50%;
    background: var(--ink-white);
  }
</style>
</head>
<body>
<main class="canvas">

  <section class="label label-front" aria-label="Front label">
    <svg class="front-split" viewBox="0 0 300 540" preserveAspectRatio="none" aria-hidden="true">
      <defs>
        <linearGradient id="stone" x1="0" x2="1" y1="0" y2="0">
          <stop offset="0" stop-color="#d6d6d6"/>
          <stop offset="1" stop-color="#efefef"/>
        </linearGradient>
      </defs>
      <path fill="url(#stone)" d="M300 0 H240 L236 18 L246 36 L238 60 L232 96 L226 130 L232 160 L222 200 L228 240 L212 268 L198 300 L206 330 L188 350 L200 380 L212 410 L198 440 L210 470 L196 500 L208 540 H300 Z"/>
    </svg>
    <span class="brand-mark" aria-hidden="true"></span>
    <h1 class="product-name"><span class="brand">Varnel</span><span class="kind">Liquid</span><span class="kind">Chalk</span></h1>
    <div class="climber-art" role="img" aria-label="White silhouette of a climber hanging from a rock edge"></div>
    <div class="sport-icons">
      <span class="sport-icon" role="img" aria-label="Weightlifting pictogram"></span>
      <span class="sport-icon" role="img" aria-label="Climbing pictogram"></span>
      <span class="sport-icon" role="img" aria-label="Gymnastics rings pictogram"></span>
      <span class="sport-icon" role="img" aria-label="Gymnastics pictogram"></span>
    </div>
  </section>

  <section class="label label-back" aria-label="Back label">
    <div class="back-copy">
      <p class="intro">Made by USA Competitive Athletes for Athletes. Increases grip and lasts 3-4 times longer than regular chalk.</p>
      <p><em>Directions:</em> Shake well. Squeeze some Varnel Liquid Chalk into your hand and rub your hands together. Let your hands air dry for about 10 seconds. To remove the chalk wash your hands with light soap.</p>
      <p><em>Warning:</em> Avoid contact with Eyes. Do not use on broken skin. Do not ingest. Keep out of reach of small children.</p>
      <p>Ingredients: Magnesium carbonate, SD Alcohol, hydroxypropylcellulose, colophonium.</p>
      <p class="cautions-title">CAUTIONS:</p>
      <ul class="cautions">
        <li>For external use only.</li>
        <li>Avoid contact with eyes discontinue use if irritation develops.</li>
        <li>Keep out of reach of children</li>
        <li>Do not expose to open flame</li>
        <li>Store in a cool or dry place</li>
      </ul>
    </div>
    <div class="back-badges">
      <span class="pill no-mess">NO MESS</span>
      <span class="pill volume">50 ML</span>
      <span class="origin-badge" aria-hidden="true"></span>
    </div>
  </section>

</main>
</body>
</html>
```